Courses Report - Analytics Redesign

We are a Learning Management System company that is looking to redesign our reporting suite in our product. We would like to add more graphs and visualizations to our reporting help communicate results and give our reporting a more modern look. Screenshots include our current courses report so that you can see the filters and type of data that our users search for. We are using Pravo Insights as our reporting service and please see https://www.pravoinsights-demo.net/visual-gallery/ for examples of what type of visualizations can be generated.

Target Market(s)

LMS Administrators, Marketing and Sales Product Trainers

Number of Pages Required

1 page

Font styles to use
Sans Serif

Colors
33b8a4
33a6d7
0392cd
00a990
85cae6
87cfc6
cadf82
abd036
9bcb3b

Requirements
Must have
• Clean and simple look. Use Raleway as font. Easy to use and intuitive filtering. Ability to add/remove filters to the output. Graphical display of results that can drill down.
Nice to have
• Better way of listing other reports in menu on left.
Should not have
• Complicated graphs that cannot be easily understood.

```html
<!DOCTYPE html>
<html lang="en">
<head>
<meta charset="utf-8">
<title>Courses Report – Analytics Redesign</title>
<link href="https://fonts.googleapis.com/css2?family=Open+Sans:wght@400;600;700&display=swap" rel="stylesheet">
<style>
:root{
  --stage:#ebebeb;
  --page:#ffffff;
  --sidebar:#0a2a36;
  --nav-active:#1a87c9;
  --sub-active:#33b8e0;
  --ink:#333c40;
  --muted:#6a7478;
  --line:#d5d9db;
  --tag:#eceeef;
  --green:#8dc63f;
  --pie-dark:#062b37;
  --pie-cyan:#29b6d8;
  --pie-teal:#1dc48b;
  --table-head:#1a87c9;
  --row-alt:#e8f2f8;
}
*{box-sizing:border-box;margin:0;padding:0}
html,body{width:1200px;height:878px;overflow:hidden;background:var(--stage);font-family:"Open Sans",Arial,sans-serif;color:var(--ink)}
.stage{position:absolute;left:0;top:0;width:1500px;height:1097px;transform:scale(.8);transform-origin:0 0}
.mockup{position:absolute;top:125px;width:596px;background:var(--page);box-shadow:0 2px 10px rgba(0,0,0,.12)}
.mockup--collapsed{left:112px;height:790px}
.mockup--expanded{left:792px;height:846px}

/* sidebar */
.sidebar{position:absolute;left:0;top:0;bottom:0;width:124px;background:var(--sidebar);color:#fff}
.brand{position:absolute;left:6px;top:12px;display:flex;align-items:center;gap:6px}
.brand-dot{width:24px;height:24px;border-radius:50%;background:var(--green)}
.brand-name{font-size:14px;font-weight:600;line-height:13px;color:#fff}
.nav-item{position:absolute;left:0;width:124px;height:19px;display:flex;align-items:center;padding-left:12px;gap:8px;font-size:8.5px}
.nav-item.is-active{background:var(--nav-active)}
.nav-icon{width:10px;height:10px;fill:#fff}
.subnav{position:absolute;left:40px;top:143px;list-style:none;font-size:7.2px;line-height:15.3px}
.subnav .is-current{color:var(--sub-active)}

/* card */
.card{position:absolute;left:144px;top:33px;width:396px;bottom:0;border:1px solid #eef0f1;border-bottom:none;pointer-events:none}
.field-label{position:absolute;left:0;width:224px;text-align:right;font-size:8.5px;font-weight:600;white-space:nowrap;transform:translateY(-50%)}
.sub-label{position:absolute;font-size:7.4px;color:var(--ink);transform:translateY(-50%)}
.input{position:absolute;left:235px;width:289px;height:23px;border:1px solid var(--line);display:flex;align-items:center;gap:4px;padding:0 5px;font-size:6.6px}
.tag{background:var(--tag);border:1px solid #dfe2e3;padding:3px 4px;white-space:nowrap}
.tag b{font-weight:400;margin-left:4px}
.select{position:absolute;left:303px;width:221px;height:23px;border:1px solid var(--line);font-size:6.6px;padding:0 8px;display:flex;align-items:center}
.select::after{content:"";position:absolute;right:0;top:0;bottom:0;width:24px;border-left:1px solid var(--line)}
.select .caret{position:absolute;right:9px;top:10px;border:3px solid transparent;border-top:3.5px solid #444}
.date{position:absolute;width:99px;height:23px;border:1px solid var(--line);font-size:6.6px;padding:0 8px;display:flex;align-items:center}
.check{position:absolute;display:flex;align-items:center;gap:4px;font-size:7px;transform:translateY(-50%);white-space:nowrap;color:var(--muted)}
.box{width:6px;height:6px;border:1px solid #8a9296;display:inline-block;position:relative;background:#fff}
.box.is-on::after{content:"";position:absolute;left:1px;top:-1px;width:2px;height:4px;border:solid #333;border-width:0 1px 1px 0;transform:rotate(40deg)}
.dd{border:2.5px solid transparent;border-top:3px solid #666;margin-top:3px}
.check--strong{color:var(--ink)}

/* results block */
.results{position:absolute;left:0;right:0;height:445px}
.btn-solid{position:absolute;left:441px;top:0;width:68px;height:24px;border-radius:12px;background:var(--green);color:#fff;font-size:6.6px;font-weight:700;display:flex;align-items:center;justify-content:center}
.btn-ghost{position:absolute;top:37px;height:22px;border:1.4px solid var(--green);border-radius:11px;color:var(--green);font-size:6.4px;font-weight:700;display:flex;align-items:center;justify-content:center}
.pie{position:absolute;left:163px;top:78px}
.legend{position:absolute;left:330px;list-style:none}
.legend li{position:absolute;left:0;display:flex;align-items:center;gap:22px;font-size:8.6px;white-space:nowrap}
.legend i{width:22px;height:20px;display:block}
.legend strong{font-weight:700;margin-right:4px}
.data-table{position:absolute;left:144px;top:239px;width:396px;border-collapse:collapse;font-size:6.4px;table-layout:fixed}
.data-table th{background:var(--table-head);color:#fff;font-weight:600;height:30px;font-size:7.4px;line-height:8px;border-right:1px solid rgba(255,255,255,.25)}
.data-table td{text-align:center;color:var(--muted);border-right:1px solid #dfe3e5;border-bottom:1px solid #dfe3e5;line-height:8px;padding:0 1px;overflow:hidden}
.data-table tr:nth-child(odd) td{background:var(--row-alt)}
.copyright{position:absolute;left:144px;width:396px;top:414px;text-align:center;font-size:6.8px;color:#555}
.page-code{position:absolute;left:573px;top:425px;font-size:6.8px;font-weight:700}
</style>
</head>
<body>
<div class="stage">

<!-- ===== Collapsed report fields ===== -->
<section class="mockup mockup--collapsed" aria-label="Courses report, report fields collapsed">
  <aside class="sidebar">
    <div class="brand"><span class="brand-dot"></span><span class="brand-name">Brightpath<br>Learning</span></div>
    <div class="nav-item" style="top:61px"><svg class="nav-icon" viewBox="0 0 10 10"><path d="M5 1 0 5h1.5v4h2.5V6.5h2V9h2.5V5H10z"/></svg>Home</div>
    <div class="nav-item" style="top:92px"><svg class="nav-icon" viewBox="0 0 10 10"><circle cx="3.5" cy="3" r="2"/><circle cx="7.5" cy="3.5" r="1.6"/><path d="M0 9c0-3 7-3 7 0zM6 9c0-2 4-2.5 4 0z"/></svg>Users</div>
    <div class="nav-item is-active" style="top:122px"><svg class="nav-icon" viewBox="0 0 10 10"><path d="M0 9h10v1H0zM1 5h1.6v4H1zM3.6 3h1.6v6H3.6zM6.2 1h1.6v8H6.2z"/></svg>Reports</div>
    <ul class="subnav"><li>Saved Reports</li><li>Users</li><li class="is-current">Courses</li><li>Due Dates</li><li>Classroom Enrollment</li><li>Course Survey</li><li>Satisfaction Survey</li><li>Purchase History</li></ul>
    <div class="nav-item" style="top:276px"><svg class="nav-icon" viewBox="0 0 10 10"><path d="M1.5 0h5l2 2v8h-7z"/></svg>Content</div>
    <div class="nav-item" style="top:306px"><svg class="nav-icon" viewBox="0 0 10 10"><circle cx="5" cy="5" r="4.5"/></svg>Site</div>
  </aside>

  <div class="field-label" style="top:67px">Groups</div>
  <div class="input" style="top:56px"><span class="tag">Sales<b>X</b></span></div>
  <div class="field-label" style="top:100px">Course Sets</div>
  <div class="input" style="top:89px"><span class="tag">Course Type Examples<b>X</b></span><span class="tag">Linkwise Learning<b>X</b></span><span class="tag">Sales Skills<b>X</b></span></div>
  <div class="field-label" style="top:133px">Course Status</div>
  <div class="input" style="top:122px">Active Courses</div>
  <div class="field-label" style="top:167px">Courses</div>
  <div class="input" style="top:156px"><span class="tag">5 Management Mistakes Blocking Sales Reps from Selling<b>X</b></span></div>
  <div class="field-label" style="top:200px">User Status</div>
  <div class="sub-label" style="top:200px;left:235px">Training Status</div>
  <div class="select" style="top:188px">Complete<span class="caret"></span></div>
  <div class="sub-label" style="top:229px;left:247px">User Status</div>
  <div class="select" style="top:218px">Active<span class="caret"></span></div>
  <div class="field-label" style="top:263px">Date Range</div>
  <div class="sub-label" style="top:270px;left:240px;text-align:center;line-height:12px">Logged in On<br>Date Range</div>
  <div class="date" style="top:252px;left:303px">01/01/2019</div>
  <div class="sub-label" style="top:263px;left:408px">To</div>
  <div class="date" style="top:252px;left:425px">01/31/2019</div>
  <div class="check check--strong" style="top:302px;left:241px"><span class="box"></span>Select All</div>
  <div class="field-label" style="top:322px">Report Fields</div>
  <div class="check" style="top:323px;left:240px"><span class="box"></span>Users<span class="dd"></span></div>
  <div class="check" style="top:323px;left:304px"><span class="box is-on"></span>Courses<span class="dd"></span></div>
  <div class="check" style="top:323px;left:386px"><span class="box"></span>Groups<span class="dd"></span></div>
  <div class="check" style="top:323px;left:458px"><span class="box"></span>Custom<span class="dd"></span></div>

  <div class="results" style="top:345px">
    <div class="field-label" style="top:12px">Report Name</div>
    <div class="input" style="top:0;width:198px;height:24px"></div>
    <div class="btn-solid">SAVE REPORT</div>
    <div class="btn-ghost" style="left:235px;width:46px">RESET</div>
    <div class="btn-ghost" style="left:290px;width:81px">GENERATE REPORT</div>
    <div class="btn-ghost" style="left:381px;width:80px">EXPORT TO EXCEL</div>
    <svg class="pie" width="140" height="140" viewBox="-70 -70 140 140" role="img" aria-label="Course progress pie chart">
      <path d="M0 0L43.7 -52.1A68 68 0 1 1 -61.6 28.7Z" fill="var(--pie-dark)"/>
      <path d="M0 0L-50.8 23.7A56 56 0 0 1 -54.1 -14.5Z" fill="var(--pie-teal)"/>
      <path d="M0 0L-58 -15.5A60 60 0 0 1 -15.5 -58Z" fill="var(--pie-cyan)"/>
      <path d="M0 0L-16 -59.9A62 62 0 0 1 39.9 -47.5Z" fill="var(--green)"/>
      <circle r="22" fill="var(--pie-dark)" opacity=".75"/>
      <circle r="10" fill="#fff"/>
      <circle r="7" fill="var(--green)"/>
      <g fill="#fff" font-size="9" font-weight="700" font-family="Open Sans, sans-serif" text-anchor="middle">
        <text x="12" y="-41">21%</text><text x="-35" y="-22">28%</text><text x="-37" y="10">11%</text><text x="22" y="37">60%</text>
      </g>
    </svg>
    <ul class="legend">
      <li style="top:98px"><i style="background:var(--pie-dark)"></i><span><strong>60%</strong>Course Completed</span></li>
      <li style="top:124px"><i style="background:var(--green)"></i><span><strong>21%</strong>Course in Progress</span></li>
      <li style="top:151px"><i style="background:var(--pie-cyan)"></i><span><strong>28%</strong>Top Learners</span></li>
      <li style="top:177px"><i style="background:var(--pie-teal)"></i><span><strong>11%</strong>Course not Started</span></li>
    </ul>
    <table class="data-table">
      <colgroup><col style="width:38px"><col style="width:36px"><col style="width:78px"><col style="width:76px"><col style="width:57px"><col style="width:55px"><col style="width:56px"></colgroup>
      <tr><th>First Name</th><th>Last Name</th><th>Email Address</th><th>Course Name</th><th>User Status</th><th>Completion Date</th><th>Job Role</th></tr>
      <tr style="height:27px"><td>Dana</td><td>Ellis</td><td>danae@brightmail.com</td><td>Determining Customer Needs</td><td>Completed</td><td>04/21/2016</td><td>Manager</td></tr>
      <tr style="height:36px"><td>Dana</td><td>Ellis</td><td>danae@brightmail.com</td><td>5 Management Mistakes Blocking Sales reps from selling</td><td>Completed</td><td>04/21/2016</td><td>Manager</td></tr>
      <tr style="height:29px"><td>Dana</td><td>Ellis</td><td>danae@brightmail.com</td><td>PDF–The LMS Evaluation Checklist</td><td>Completed</td><td>04/21/2016</td><td>Manager</td></tr>
      <tr style="height:26px"><td>Dana</td><td>Ellis</td><td>danae@brightmail.com</td><td>Health and Wellness</td><td>Completed</td><td>04/21/2016</td><td>Manager</td></tr>
    </table>
    <p class="copyright">Copyright © 2019, Brightpath Learning. All rights reserved.</p>
    <p class="page-code">C17</p>
  </div>
  <div class="card"></div>
</section>

<!-- ===== Expanded report fields ===== -->
<section class="mockup mockup--expanded" aria-label="Courses report, course fields expanded">
  <aside class="sidebar">
    <div class="brand"><span class="brand-dot"></span><span class="brand-name">Brightpath<br>Learning</span></div>
    <div class="nav-item" style="top:61px"><svg class="nav-icon" viewBox="0 0 10 10"><path d="M5 1 0 5h1.5v4h2.5V6.5h2V9h2.5V5H10z"/></svg>Home</div>
    <div class="nav-item" style="top:92px"><svg class="nav-icon" viewBox="0 0 10 10"><circle cx="3.5" cy="3" r="2"/><circle cx="7.5" cy="3.5" r="1.6"/><path d="M0 9c0-3 7-3 7 0zM6 9c0-2 4-2.5 4 0z"/></svg>Users</div>
    <div class="nav-item is-active" style="top:122px"><svg class="nav-icon" viewBox="0 0 10 10"><path d="M0 9h10v1H0zM1 5h1.6v4H1zM3.6 3h1.6v6H3.6zM6.2 1h1.6v8H6.2z"/></svg>Reports</div>
    <ul class="subnav"><li>Saved Reports</li><li>Users</li><li class="is-current">Courses</li><li>Due Dates</li><li>Classroom Enrollment</li><li>Course Survey</li><li>Satisfaction Survey</li><li>Purchase History</li></ul>
    <div class="nav-item" style="top:276px"><svg class="nav-icon" viewBox="0 0 10 10"><path d="M1.5 0h5l2 2v8h-7z"/></svg>Content</div>
    <div class="nav-item" style="top:306px"><svg class="nav-icon" viewBox="0 0 10 10"><circle cx="5" cy="5" r="4.5"/></svg>Site</div>
  </aside>

  <div class="field-label" style="top:67px">Groups</div>
  <div class="input" style="top:56px"><span class="tag">Sales<b>X</b></span></div>
  <div class="field-label" style="top:100px">Course Sets</div>
  <div class="input" style="top:89px"><span class="tag">Course Type Examples<b>X</b></span><span class="tag">Linkwise Learning<b>X</b></span><span class="tag">Sales Skills<b>X</b></span></div>
  <div class="field-label" style="top:133px">Course Status</div>
  <div class="input" style="top:122px">Active Courses</div>
  <div class="field-label" style="top:167px">Courses</div>
  <div class="input" style="top:156px"><span class="tag">5 Management Mistakes Blocking Sales Reps from Selling<b>X</b></span></div>
  <div class="field-label" style="top:200px">User Status</div>
  <div class="sub-label" style="top:200px;left:235px">Training Status</div>
  <div class="select" style="top:188px">Complete<span class="caret"></span></div>
  <div class="sub-label" style="top:229px;left:247px">User Status</div>
  <div class="select" style="top:218px">Active<span class="caret"></span></div>
  <div class="field-label" style="top:263px">Date Range</div>
  <div class="sub-label" style="top:270px;left:240px;text-align:center;line-height:12px">Logged in On<br>Date Range</div>
  <div class="date" style="top:252px;left:303px">01/01/2019</div>
  <div class="sub-label" style="top:263px;left:408px">To</div>
  <div class="date" style="top:252px;left:425px">01/31/2019</div>
  <div class="check check--strong" style="top:302px;left:241px"><span class="box"></span>Select All</div>
  <div class="field-label" style="top:322px">Report Fields</div>
  <div class="check" style="top:323px;left:240px"><span class="box"></span>Users<span class="dd"></span></div>
  <div class="check" style="top:323px;left:304px"><span class="box is-on"></span>Courses<span class="dd"></span></div>
  <div class="check" style="top:323px;left:386px"><span class="box"></span>Groups<span class="dd"></span></div>
  <div class="check" style="top:323px;left:458px"><span class="box"></span>Custom<span class="dd"></span></div>
  <div class="check" style="top:336px;left:314px"><span class="box is-on"></span>Courses: Course Name</div>
  <div class="check" style="top:349px;left:314px"><span class="box is-on"></span>Courses: User Status</div>
  <div class="check" style="top:362px;left:314px"><span class="box is-on"></span>Courses: Completion Date</div>
  <div class="check" style="top:376px;left:314px"><span class="box"></span>Courses: User Score</div>
  <div class="check" style="top:389px;left:314px"><span class="box"></span>Courses: User Session Time</div>

  <div class="results" style="top:400px">
    <div class="field-label" style="top:12px">Report Name</div>
    <div class="input" style="top:0;width:198px;height:24px"></div>
    <div class="btn-solid">SAVE REPORT</div>
    <div class="btn-ghost" style="left:235px;width:46px">RESET</div>
    <div class="btn-ghost" style="left:290px;width:81px">GENERATE REPORT</div>
    <div class="btn-ghost" style="left:381px;width:80px">EXPORT TO EXCEL</div>
    <svg class="pie" width="140" height="140" viewBox="-70 -70 140 140" role="img" aria-label="Course progress pie chart">
      <path d="M0 0L43.7 -52.1A68 68 0 1 1 -61.6 28.7Z" fill="var(--pie-dark)"/>
      <path d="M0 0L-50.8 23.7A56 56 0 0 1 -54.1 -14.5Z" fill="var(--pie-teal)"/>
      <path d="M0 0L-58 -15.5A60 60 0 0 1 -15.5 -58Z" fill="var(--pie-cyan)"/>
      <path d="M0 0L-16 -59.9A62 62 0 0 1 39.9 -47.5Z" fill="var(--green)"/>
      <circle r="22" fill="var(--pie-dark)" opacity=".75"/>
      <circle r="10" fill="#fff"/>
      <circle r="7" fill="var(--green)"/>
      <g fill="#fff" font-size="9" font-weight="700" font-family="Open Sans, sans-serif" text-anchor="middle">
        <text x="12" y="-41">21%</text><text x="-35" y="-22">28%</text><text x="-37" y="10">11%</text><text x="22" y="37">60%</text>
      </g>
    </svg>
    <ul class="legend">
      <li style="top:98px"><i style="background:var(--pie-dark)"></i><span><strong>60%</strong>Course Completed</span></li>
      <li style="top:124px"><i style="background:var(--green)"></i><span><strong>21%</strong>Course in Progress</span></li>
      <li style="top:151px"><i style="background:var(--pie-cyan)"></i><span><strong>28%</strong>Top Learners</span></li>
      <li style="top:177px"><i style="background:var(--pie-teal)"></i><span><strong>11%</strong>Course not Started</span></li>
    </ul>
    <table class="data-table">
      <colgroup><col style="width:38px"><col style="width:36px"><col style="width:78px"><col style="width:76px"><col style="width:57px"><col style="width:55px"><col style="width:56px"></colgroup>
      <tr><th>First Name</th><th>Last Name</th><th>Email Address</th><th>Course Name</th><th>User Status</th><th>Completion Date</th><th>Job Role</th></tr>
      <tr style="height:27px"><td>Dana</td><td>Ellis</td><td>danae@brightmail.com</td><td>Determining Customer Needs</td><td>Completed</td><td>04/21/2016</td><td>Manager</td></tr>
      <tr style="height:36px"><td>Dana</td><td>Ellis</td><td>danae@brightmail.com</td><td>5 Management Mistakes Blocking Sales reps from selling</td><td>Completed</td><td>04/21/2016</td><td>Manager</td></tr>
      <tr style="height:29px"><td>Dana</td><td>Ellis</td><td>danae@brightmail.com</td><td>PDF–The LMS Evaluation Checklist</td><td>Completed</td><td>04/21/2016</td><td>Manager</td></tr>
      <tr style="height:26px"><td>Dana</td><td>Ellis</td><td>danae@brightmail.com</td><td>Health and Wellness</td><td>Completed</td><td>04/21/2016</td><td>Manager</td></tr>
    </table>
    <p class="copyright">Copyright © 2019, Brightpath Learning. All rights reserved.</p>
    <p class="page-code">C17</p>
  </div>
  <div class="card"></div>
</section>

</div>
</body>
</html>
```